Lumex

Hello Artboardly Community,

Thank you for participating in designing Snapquill App. So far I've received some amazing looking designs!
Unfortunately, Some of the designs being submitted are not following the project brief.
The screens you submit should be designed "1:1 / Exactly" according to the project brief.
Updates

Target Market(s)

Millennials

Industry/Entity Type

Community

Font styles to use
Sans Serif

Requirements
Must have
• Follow the project brief exactly.

```html
<!DOCTYPE html>
<html lang="en">
<head>
<meta charset="utf-8">
<title>Snapquill – App Screens</title>
<link rel="stylesheet" href="https://fonts.googleapis.com/css2?family=Raleway:wght@300;400;600&family=Montserrat:wght@300;400;600&family=Libre+Baskerville&display=swap">
<style>
:root{
  --stage:#292929;
  --capture-bg:#888888;
  --white:#ffffff;
  --ink:#444444;
  --feed-bg:#e6e8ea;
  --ring:#c9c9c9;
  --accent:#8fd14f;
  --line:#9a9a9a;
}
*{box-sizing:border-box;margin:0;padding:0}
html,body{width:1200px;height:1000px;overflow:hidden}
body{background:var(--stage);position:relative;font-family:"Raleway",sans-serif}
.screen{position:absolute;top:75px;width:479px;height:851px;overflow:hidden}
.screen--capture{left:100px;background:var(--capture-bg)}
.screen--feed{left:623px;background:var(--feed-bg)}
.abs{position:absolute}
.app-name{left:60px;top:20px;color:var(--white);font:600 24px "Raleway",sans-serif;letter-spacing:-.2px}
.prompt{left:0;width:100%;top:370px;text-align:center;color:var(--white);font:300 24px "Raleway",sans-serif}
.shutter{left:189px;top:724px;width:100px;height:100px;border-radius:50%;background:var(--ring)}
.shutter-inner{left:10px;top:10px;width:80px;height:80px;border-radius:50%;background:var(--white);display:flex;align-items:center;justify-content:center}
.feed-header{left:0;top:0;width:100%;height:70px;background:var(--white)}
.filter-label{left:62px;top:22px;color:var(--ink);font:400 20px "Raleway",sans-serif}
.tile{position:absolute;overflow:hidden}
.tile-title{position:absolute;left:0;width:100%;text-align:center}
.sculp{left:8px;top:80px;width:226px;height:227px;background:radial-gradient(circle at 55% 45%,#8a8886,#4a4a4a 80%)}
.sculp .tile-title{top:90px;color:var(--white);font:300 38px "Montserrat",sans-serif;letter-spacing:4px}
.oceania{left:244px;top:80px;width:227px;height:113px;background:linear-gradient(180deg,#2d7fb8,#0f3a63)}
.oceania .tile-title{top:44px;color:var(--white);font:300 21px "Montserrat",sans-serif;letter-spacing:8px}
.nature{left:244px;top:203px;width:227px;height:316px;background:linear-gradient(180deg,#f7f3ef 0%,#d9ddd7 30%,#3c5a48 70%,#1f3a2c)}
.nature .t1{top:68px;color:#222;font:400 20px "Montserrat",sans-serif;letter-spacing:6px}
.nature .t2{top:92px;color:#111;font:600 20px "Montserrat",sans-serif}
.art{left:8px;top:316px;width:226px;height:311px;background:linear-gradient(150deg,#f4c9b8,#f3e3c8 40%,#4fa89a 65%,#e89aa4)}
.art .tile-title{top:20px;color:var(--white);font:600 150px/.9 "Montserrat",sans-serif;letter-spacing:-6px;text-align:left;left:10px}
.slate{left:244px;top:528px;width:227px;height:227px;background:linear-gradient(135deg,#2a2a2a,#1a1a1a 50%,#4b4fd8 62%,#222)}
.expressions{left:8px;top:636px;width:226px;height:215px;background:var(--white)}
.expressions .tile-title{top:38px;color:#111;font:400 30px "Raleway",sans-serif;letter-spacing:-1.5px}
.expressions .plates{left:14px;top:99px;width:198px;height:120px;background:linear-gradient(90deg,#1a1a1a,#d8d8d8,#1a1a1a)}
.orvak{left:244px;top:764px;width:227px;height:90px;background:#efefeb;color:#333;font:400 16px/17px "Libre Baskerville",serif;padding:14px 13px}
.orvak p+p{margin-top:18px}
.compose{left:381px;top:747px;width:84px;height:84px;border-radius:50%;background:var(--white);border:4px solid var(--ring);display:flex;align-items:center;justify-content:center}
</style>
</head>
<body>

<section class="screen screen--capture">
  <svg class="abs" style="left:17px;top:24px" width="25" height="18" viewBox="0 0 25 18"><g stroke="#fff" stroke-width="2.5"><line x1="0" y1="2" x2="25" y2="2"/><line x1="0" y1="9" x2="25" y2="9"/><line x1="0" y1="16" x2="25" y2="16"/></g></svg>
  <div class="abs app-name">Snapquill</div>
  <svg class="abs" style="left:432px;top:21px" width="27" height="27" viewBox="0 0 27 27" fill="none" stroke="#fff" stroke-width="1.3"><rect x=".7" y=".7" width="25.6" height="25.6" rx="2"/><rect x="4" y="4" width="9" height="7"/><line x1="15" y1="5" x2="23" y2="5"/><line x1="15" y1="9" x2="23" y2="9"/><line x1="4" y1="14" x2="23" y2="14"/><line x1="4" y1="18" x2="23" y2="18"/><line x1="4" y1="22" x2="23" y2="22"/></svg>
  <div class="abs prompt">Type something...</div>
  <svg class="abs" style="left:72px;top:758px" width="36" height="36" viewBox="0 0 36 36" fill="none" stroke="#fff" stroke-width="1.4"><rect x=".7" y=".7" width="15" height="34.6"/><rect x="19" y=".7" width="16.3" height="15.5"/><rect x="19" y="19" width="16.3" height="16.3"/></svg>
  <div class="abs shutter"><div class="abs shutter-inner">
    <svg width="34" height="26" viewBox="0 0 34 26" fill="none" stroke="var(--accent)" stroke-width="1.6"><path d="M2 6h8l3-4h8l3 4h8v18H2z"/><circle cx="17" cy="14" r="6"/></svg>
  </div></div>
  <svg class="abs" style="left:361px;top:758px" width="34" height="34" viewBox="0 0 34 34" stroke="#fff" stroke-width="1.4"><line x1="17" y1="0" x2="17" y2="34"/><line x1="0" y1="17" x2="34" y2="17"/></svg>
</section>

<section class="screen screen--feed">
  <header class="abs feed-header">
    <svg class="abs" style="left:17px;top:26px" width="25" height="17" viewBox="0 0 25 17"><g stroke="#555" stroke-width="2"><line x1="0" y1="1.5" x2="25" y2="1.5"/><line x1="0" y1="8.5" x2="25" y2="8.5"/><line x1="0" y1="15.5" x2="25" y2="15.5"/></g></svg>
    <div class="abs filter-label">All Files</div>
    <svg class="abs" style="left:148px;top:29px" width="20" height="12" viewBox="0 0 20 12" fill="none" stroke="#555" stroke-width="1.6"><path d="M1 1l9 9 9-9"/></svg>
    <svg class="abs" style="left:430px;top:21px" width="28" height="28" viewBox="0 0 28 28" fill="none" stroke="#777" stroke-width="1.4"><rect x=".7" y=".7" width="26.6" height="26.6"/><line x1="12" y1="0" x2="12" y2="28"/><line x1="12" y1="14" x2="28" y2="14"/></svg>
  </header>

  <article class="tile sculp" role="img" aria-label="Photo of an abstract stone sculpture with red splashes"><div class="tile-title">SCULP</div></article>
  <article class="tile oceania" role="img" aria-label="Underwater photo of a school of fish in blue water"><div class="tile-title">OCEANIA</div></article>
  <article class="tile nature" role="img" aria-label="Photo of a misty pine forest"><div class="tile-title t1">NATURE</div><div class="tile-title t2">BEHAVIOUR</div></article>
  <article class="tile art" role="img" aria-label="Pastel geometric illustration"><div class="tile-title">ART</div></article>
  <article class="tile slate" role="img" aria-label="Photo of magazine app screens laid out on a dark surface"></article>
  <article class="tile expressions"><div class="tile-title">EXPRESSIONS</div><div class="abs plates" role="img" aria-label="Row of black and white abstract poster illustrations"></div></article>
  <article class="tile orvak"><p>ORVAK<br>UNIVERSE</p><p>Orvak + Finchley</p></article>

  <div class="abs compose">
    <svg width="24" height="34" viewBox="0 0 24 34" fill="none" stroke="#888" stroke-width="1.4"><path d="M18 2l4 3-13 23-5 4 1-6z"/><line x1="16" y1="6" x2="20" y2="9"/></svg>
  </div>
</section>

</body>
</html>
```